KT Prime Motion personal training needs a new Business Card design for 2016

Business Card design:
Our current business card is very plain
We are bringing on our first team member next year and thought its a perfect time to have a new face lift for our company!

We are a Personal Training business "KT Prime Motion" who specializes in strength and conditioning / weightloss training,
We also run a yearly Bootcamp called "Ferocity Drillcamps", this is our Logo Design which we are looking for

The pink and blue in the logo are our business colours, how ever we don't want those colours to heavily dominate the card.

We are looking for a business card which is eye catching, and creative.

I am open to suggestions and any designs :)

Logo Design:

For our Logo Design we are looking for a bright, energetic logo, preferably a word logo which portrays strength and high intensity
If it has icon's etc in it thats fine again im open for suggestions :)
The Logo Design is for our Bootcamp which runs yearly
The bootcamp is called "Ferocity Drillcamp"

Target Market(s)

Age 20-40
Individuals who want to look great and have more energy

Industry/Entity Type

Business

Contact Information for Business Card

On the front
KT Prime Motion Doriel Maxton Personal Training / Bootcamps / Pilates / Nutrition Healthy mind, Healthy body, Ultimate lifestyle < our slogan
Icons for the following
Email:
Mobile:
Facebook:
Instagram:

On the back we would like to include somewhere
"Show this card to receive 50% off your first 30min pt session"
"Valid to one user only"

Logo Text

Ferocity Drillcamp

Font styles to use
Serif

Colors
e34197
0255a3
000000
ffffff

Requirements
Must have
• - Icons for instagram, facebook, email and mobile phone
• - Slogan: Healthy mind, Healthy body, Ultimate lifestyle
• - What we offer: Personal Training , Bootcamps, Pilates, Nutrition
• - Logo
• -
Nice to have
• - Our 50% offer on the back
• - a place for a photo
Should not have
• - Pink and Blue everywhere

```html
<!DOCTYPE html>
<html lang="en">
<head>
<meta charset="utf-8">
<title>KT Prime Motion – Business Card</title>
<link href="https://fonts.googleapis.com/css2?family=Open+Sans:wght@400;700&family=Noto+Serif:wght@400&display=swap" rel="stylesheet">
<style>
  :root {
    --pink: #e34197;
    --pink-soft: #f0a3cc;
    --blue: #0255a3;
    --blue-light: #3a9ad9;
    --black: #000000;
    --white: #ffffff;
    --grey: #555555;
    --page: #ecebe8;
  }
  * { margin: 0; padding: 0; box-sizing: border-box; }
  html, body { width: 1200px; height: 1062px; overflow: hidden; background: var(--page); }
  body { position: relative; font-family: "Open Sans", sans-serif; }

  .card {
    position: absolute; left: 180px; width: 840px; height: 480px;
    overflow: hidden; border-radius: 4px;
    box-shadow: 0 6px 20px rgba(0,0,0,.25);
  }
  .card-front { top: 36px; }
  .card-back { top: 546px; background: linear-gradient(160deg, #2b2b2b 0%, #0d0d0d 45%, #000 100%); }
  .card-shape { position: absolute; inset: 0; }

  /* front */
  .brand { position: absolute; left: 50px; top: 250px; display: flex; align-items: center; gap: 14px; white-space: nowrap; }
  .brand-dot { flex: none; width: 62px; height: 62px; border-radius: 50%; background: var(--blue-light); }
  .brand-name { font-weight: 700; font-size: 32px; color: var(--blue-light); letter-spacing: .5px; }

  .divider { position: absolute; left: 450px; top: 150px; width: 1px; height: 160px; background: linear-gradient(var(--white), var(--blue-light), var(--white)); }

  .contact { position: absolute; left: 482px; top: 112px; }
  .contact-name { font-weight: 700; font-size: 24px; color: var(--blue); line-height: 1.1; }
  .contact-role { font-size: 16px; color: var(--grey); margin-bottom: 14px; }
  .contact-list { list-style: none; }
  .contact-item { display: flex; align-items: center; gap: 12px; font-size: 16px; color: #333; margin-bottom: 8px; white-space: nowrap; }
  .contact-icon { flex: none; width: 28px; height: 28px; background: var(--blue); display: flex; align-items: center; justify-content: center; }
  .contact-icon svg { width: 16px; height: 16px; }

  .tagline { position: absolute; left: 60px; top: 380px; right: 40px; font-size: 17px; line-height: 1.45; color: var(--blue-light); }

  /* back */
  .photo {
    position: absolute; right: 70px; top: 34px; width: 140px; height: 140px; border-radius: 50%;
    border: 4px solid var(--white); background: radial-gradient(circle at 50% 40%, #5aa9e6, #1f6fb8 70%);
  }
  .offer { position: absolute; left: 70px; top: 200px; font-family: "Noto Serif", serif; }
  .offer-main { font-size: 34px; color: var(--blue-light); }
  .offer-main .accent { color: var(--pink); }
  .offer-note { font-size: 22px; color: var(--blue-light); margin-top: 12px; margin-left: 60px; }
  .back-brand { position: absolute; right: 70px; bottom: 40px; display: flex; align-items: center; gap: 14px; white-space: nowrap; }
  .back-brand .brand-dot { width: 48px; height: 48px; }
  .back-brand .brand-name { font-size: 28px; }
</style>
</head>
<body>

<section class="card card-front">
  <svg class="card-shape" viewBox="0 0 840 480" preserveAspectRatio="none" aria-hidden="true">
    <rect width="840" height="480" fill="var(--black)"/>
    <path d="M0,236 Q300,40 840,-10 L840,480 L0,480 Z" fill="var(--pink)"/>
    <path d="M0,250 Q300,58 840,8 L840,480 L0,480 Z" fill="var(--pink-soft)"/>
    <path d="M0,262 Q300,72 840,22 L840,480 L0,480 Z" fill="var(--white)"/>
  </svg>

  <div class="brand">
    <span class="brand-dot"></span>
    <span class="brand-name">KT Prime Motion</span>
  </div>

  <div class="divider"></div>

  <div class="contact">
    <p class="contact-name">Corin Vale</p>
    <p class="contact-role">Manager</p>
    <ul class="contact-list">
      <li class="contact-item">
        <span class="contact-icon"><svg viewBox="0 0 16 16"><rect x="4" y="1" width="8" height="14" rx="1.5" fill="none" stroke="#fff" stroke-width="1.6"/><circle cx="8" cy="12.5" r="1" fill="#fff"/></svg></span>
        555.018.2741
      </li>
      <li class="contact-item">
        <span class="contact-icon"><svg viewBox="0 0 16 16"><rect x="1.5" y="3.5" width="13" height="9" fill="none" stroke="#fff" stroke-width="1.5"/><path d="M1.5 3.5 L8 9 L14.5 3.5" fill="none" stroke="#fff" stroke-width="1.5"/></svg></span>
        hello@ktprimemotion.com
      </li>
      <li class="contact-item">
        <span class="contact-icon"><svg viewBox="0 0 16 16"><path d="M1.5 5 H5 L6.2 3 H9.8 L11 5 H14.5 V13 H1.5 Z" fill="none" stroke="#fff" stroke-width="1.4" stroke-linejoin="round"/><circle cx="8" cy="9" r="2.3" fill="none" stroke="#fff" stroke-width="1.4"/></svg></span>
        ktprime@pixgram.net
      </li>
      <li class="contact-item">
        <span class="contact-icon"><svg viewBox="0 0 16 16"><circle cx="8" cy="8" r="6.3" fill="none" stroke="#fff" stroke-width="1.3"/><ellipse cx="8" cy="8" rx="2.8" ry="6.3" fill="none" stroke="#fff" stroke-width="1.1"/><path d="M1.7 8 H14.3" stroke="#fff" stroke-width="1.1"/></svg></span>
        www.friendwall.net/ktprime
      </li>
    </ul>
  </div>

  <p class="tagline">KT Prime Motion Doriel Maxton Personal Training Bootcamps / Pilates<br>Nutrition Healthy mind, Healthy body, Ultimate lifestyle</p>
</section>

<section class="card card-back">
  <div class="photo" role="img" aria-label="Portrait photo of the trainer"></div>
  <div class="offer">
    <p class="offer-main">receive <span class="accent">50%</span> off your first 30min pt session</p>
    <p class="offer-note">"Valid to one user only"</p>
  </div>
  <div class="back-brand">
    <span class="brand-dot"></span>
    <span class="brand-name">KT Prime Motion</span>
  </div>
</section>

</body>
</html>
```